Plumbing Company After Business Card

Business card for a plumbing business that offers a variety of plumbing services including maintenance, domestic and commercial plumbing. My main focus is to offer high quality professional service. A logo on the card would be ideal. Any other questions feel free to email. Cheers

Looking for something modern and upmarket with preferably a matte black background

Business name is Keystone Plumbing and Gas

Industry/Entity Type

Plumbing

Contact Information for Business Card

Keystone Plumbing and Gas
Marcus Thornell
0427915368
14 Corrigan Road, Elmvale 3561
keystoneplumbing@mailbay.com.au
ABN 52 647 183 925

Font styles to use
Sans Serif

Colors
1b1b1b
ffffff
3377b5

Requirements
Must have
• Domestic
• Commercial
• Maintenance

```html
<!DOCTYPE html>
<html lang="en">
<head>
<meta charset="utf-8">
<title>Keystone Plumbing and Gas – Business Card</title>
<link rel="stylesheet" href="https://fonts.googleapis.com/css2?family=Fira+Sans+Condensed:wght@500&family=Open+Sans:wght@400;600&display=swap">
<style>
  :root {
    --brand-blue: #3377b5;
    --paper: #ffffff;
    --ink: #1b1b1b;
    --backdrop: #e9e9eb;
  }
  * { margin: 0; padding: 0; box-sizing: border-box; }
  html, body { width: 1200px; height: 900px; overflow: hidden; }
  body {
    position: relative;
    background: var(--backdrop);
    font-family: "Open Sans", sans-serif;
    color: var(--ink);
  }
  .card {
    position: absolute;
    border-radius: 16px;
    overflow: hidden;
    box-shadow: 0 6px 20px rgba(0,0,0,0.12);
  }
  .card--front { left: 78px; top: 34px; width: 587px; height: 364px; background: var(--paper); }
  .card--back  { left: 390px; top: 506px; width: 565px; height: 350px; background: var(--brand-blue); }

  .band { position: absolute; left: 0; right: 0; }
  .card--front .band { top: 29px; height: 99px; background: var(--brand-blue); }
  .card--back .band  { top: 81px; height: 96px; background: var(--paper); }

  .brand-mark {
    position: absolute;
    border-radius: 50%;
    display: flex; align-items: center; justify-content: center;
    font-family: "Fira Sans Condensed", sans-serif;
    font-weight: 500;
    font-size: 24px;
  }
  .card--front .brand-mark {
    left: 226px; top: 9px; width: 140px; height: 140px;
    background: var(--paper); color: var(--brand-blue);
  }
  .card--back .brand-mark {
    left: 219px; top: 67px; width: 124px; height: 124px;
    background: var(--brand-blue); color: var(--paper);
  }

  .company-name {
    position: absolute; left: 0; right: 0;
    text-align: center;
    font-family: "Fira Sans Condensed", sans-serif;
    font-weight: 500;
    font-size: 31px;
    letter-spacing: 0.2px;
  }
  .services {
    position: absolute; left: 0; right: 0;
    text-align: center;
    font-size: 15px;
  }
  .card--front .company-name { top: 148px; left: 0; width: 646px; color: var(--brand-blue); }
  .card--front .services { top: 184px; width: 590px; color: var(--ink); }
  .card--back .company-name { top: 190px; width: 563px; color: var(--paper); font-size: 29px; }
  .card--back .services { top: 226px; width: 563px; color: var(--paper); font-size: 14px; }

  .person-name {
    position: absolute; left: 192px; top: 233px;
    font-weight: 600; font-size: 21px; color: var(--brand-blue);
  }
  .contact {
    position: absolute; font-size: 15px; color: var(--ink);
    display: flex; align-items: center; gap: 8px;
  }
  .contact--phone { right: 291px; top: 293px; }
  .contact--email { right: 291px; top: 319px; }
  .contact--abn { left: 327px; top: 287px; }
  .contact--address { left: 327px; top: 320px; }
  .contact .label { font-weight: 600; }
  .icon { width: 14px; height: 14px; fill: var(--brand-blue); }
</style>
</head>
<body>

  <section class="card card--front">
    <div class="band"></div>
    <div class="brand-mark">Keystone</div>
    <h1 class="company-name">Keystone Plumbing and Gas</h1>
    <p class="services">Domestic | Commercial | Maintenance</p>
    <p class="person-name">Marcus Thornell</p>

    <p class="contact contact--phone">0427915368
      <svg class="icon" viewBox="0 0 24 24" aria-hidden="true"><path d="M6.6 10.8a15.1 15.1 0 0 0 6.6 6.6l2.2-2.2c.3-.3.7-.4 1-.2 1.1.4 2.3.6 3.6.6.6 0 1 .4 1 1V20c0 .6-.4 1-1 1A17 17 0 0 1 3 4c0-.6.4-1 1-1h3.5c.6 0 1 .4 1 1 0 1.3.2 2.5.6 3.6.1.3 0 .7-.2 1z"/></svg>
    </p>
    <p class="contact contact--email">keystoneplumbing@mailbay.com.au
      <svg class="icon" viewBox="0 0 24 24" aria-hidden="true"><path d="M2 5h20v14H2zm2 2v.5l8 5 8-5V7l-8 5z"/></svg>
    </p>
    <p class="contact contact--abn"><span class="label">ABN:</span> 52 647 183 925</p>
    <p class="contact contact--address">14 Corrigan Road, Elmvale 3561</p>
  </section>

  <section class="card card--back">
    <div class="band"></div>
    <div class="brand-mark">Keystone</div>
    <h2 class="company-name">Keystone Plumbing and Gas</h2>
    <p class="services">Domestic | Commercial | Maintenance</p>
  </section>

</body>
</html>
```